Varn Tolq, Inc. Business Cards/Stationary
Business Cards/Stationary/Letterhead
Attention all:
email is kholbeck@brantovaseal.org
Sorry for the mistake…it doesn't detract from the excellent designs!
I will likely select a winner soon, within the next day or two…
Karl Holbeck
Can you show me where the Name and Title would go on #1,#2,#3,#4…?
Also…on the back of the card…I love the map/Logo. Can we put the www.brantovaseal.org under it?
On numbers #1-#7 - is that a white background? Off-white? Soft gray? Silver? I really like it -- contrasts beautifully with the red, black, and blue...
RW/TPH/FE Team.

```html
<!DOCTYPE html>
<html lang="en">
<head>
<meta charset="utf-8">
<title>Varn Tolq, Inc. Stationery Concepts</title>
<link rel="stylesheet" href="https://fonts.googleapis.com/css2?family=Tinos:wght@400;700&family=Open+Sans:wght@400;600&display=swap">
<style>
  :root {
    --backdrop: #4a3428;
    --paper: #ffffff;
    --paper-edge: #e6e6e6;
    --ink: #1a1a1a;
    --ink-soft: #555555;
    --brand-black: #111111;
    --brand-red: #9c1518;
    --label: #e9e2da;
  }
  * { box-sizing: border-box; margin: 0; padding: 0; }
  html, body { width: 1200px; height: 466px; overflow: hidden; }
  body {
    background: var(--backdrop);
    position: relative;
    font-family: "Open Sans", sans-serif;
  }
  .piece { position: absolute; background: var(--paper); box-shadow: 0 2px 6px rgba(0,0,0,.45); overflow: hidden; }
  .piece svg.trim { position: absolute; inset: 0; width: 100%; height: 100%; }
  .label {
    position: absolute;
    font-size: 6.5px; letter-spacing: 1.5px; text-transform: uppercase;
    color: var(--label); text-align: center;
  }
  .set-title { left: 12px; top: 178px; width: 110px; font-size: 7.5px; letter-spacing: 2px; text-align: left; }
  .wordmark {
    position: absolute;
    font-family: "Tinos", serif; font-weight: 700; color: var(--ink);
    white-space: nowrap;
  }
  .contact { position: absolute; font-size: 3.2px; line-height: 1.5; color: var(--ink-soft); white-space: nowrap; }

  /* business cards */
  .card { left: 14px; width: 104px; height: 60px; }
  .card-front { top: 208px; }
  .card-back { top: 292px; }
  .card-front .wordmark { left: 7px; top: 6px; font-size: 9px; }
  .card-front .contact { left: 7px; top: 34px; }
  .card-back .wordmark { left: 0; right: 0; top: 22px; text-align: center; font-size: 11px; }
  .card-front-label { left: 14px; top: 272px; width: 104px; }
  .card-back-label { left: 14px; top: 356px; width: 104px; }

  /* letterheads */
  .letterhead { top: 24px; width: 391px; height: 420px; }
  .letterhead-one { left: 137px; }
  .letterhead-two { left: 545px; }
  .letterhead .wordmark { left: 22px; top: 20px; font-size: 15px; }
  .letterhead-one .contact { left: 22px; top: 376px; font-size: 4px; }
  .letterhead-two .contact { left: 90px; top: 404px; font-size: 4px; color: #dddddd; }
  .letterhead-one-label { left: 137px; top: 450px; width: 391px; }
  .letterhead-two-label { left: 545px; top: 450px; width: 391px; }

  /* envelopes */
  .envelope-back { left: 962px; width: 214px; height: 66px; }
  .envelope-back.black { top: 24px; }
  .envelope-back.red { top: 100px; }
  .envelope-back.white { top: 176px; }
  .envelope-front { left: 962px; top: 300px; width: 214px; height: 134px; }
  .envelope-front .wordmark { left: 10px; top: 10px; font-size: 9px; }
  .envelope-front .contact { left: 10px; top: 26px; }
  .envelope-label { left: 962px; top: 440px; width: 214px; }
</style>
</head>
<body>
  <div class="label set-title">Stationery Concepts</div>

  <!-- business card front -->
  <div class="piece card card-front">
    <svg class="trim" viewBox="0 0 104 60" preserveAspectRatio="none" aria-hidden="true">
      <path d="M86 0 Q100 30 80 60 L104 60 L104 0 Z" fill="var(--brand-black)"/>
      <path d="M104 22 Q100 48 78 60 L92 60 Q104 46 104 34 Z" fill="var(--brand-red)"/>
    </svg>
    <div class="wordmark">Varn Tolq, Inc.</div>
    <div class="contact">Karl Holbeck<br>RW/TPH/FE Team<br>Tel 555 010 2244<br>kholbeck@brantovaseal.org<br>www.brantovaseal.org</div>
  </div>
  <div class="label card-front-label">Business Card Front</div>

  <!-- business card back -->
  <div class="piece card card-back">
    <svg class="trim" viewBox="0 0 104 60" preserveAspectRatio="none" aria-hidden="true">
      <path d="M0 44 Q40 50 104 40 L104 60 L0 60 Z" fill="var(--brand-black)"/>
      <path d="M0 50 Q50 56 104 48 L104 54 Q50 60 0 56 Z" fill="var(--brand-red)"/>
    </svg>
    <div class="wordmark">Varn Tolq, Inc.</div>
  </div>
  <div class="label card-back-label">Business Card Back</div>

  <!-- letterhead option 1 -->
  <div class="piece letterhead letterhead-one">
    <svg class="trim" viewBox="0 0 391 420" preserveAspectRatio="none" aria-hidden="true">
      <path d="M340 0 Q400 160 352 420 L391 420 L391 0 Z" fill="var(--brand-black)"/>
      <path d="M391 150 Q392 330 300 420 L352 420 Q385 320 391 230 Z" fill="var(--brand-red)"/>
    </svg>
    <div class="wordmark">Varn Tolq, Inc.</div>
    <div class="contact">120 Harbor Lane, Suite 4<br>Norvale, TX 70000<br>Tel 555 010 2244<br>kholbeck@brantovaseal.org<br>www.brantovaseal.org</div>
  </div>
  <div class="label letterhead-one-label">Letter Head Option 1</div>

  <!-- letterhead option 2 -->
  <div class="piece letterhead letterhead-two">
    <svg class="trim" viewBox="0 0 391 420" preserveAspectRatio="none" aria-hidden="true">
      <path d="M0 300 Q120 380 391 392 L391 420 L0 420 Z" fill="var(--brand-black)"/>
      <path d="M0 318 Q70 370 150 388 Q60 385 0 360 Z" fill="var(--brand-red)"/>
      <path d="M0 290 Q30 340 120 372 Q40 350 0 310 Z" fill="var(--brand-red)"/>
    </svg>
    <div class="wordmark">Varn Tolq, Inc.</div>
    <div class="contact">120 Harbor Lane, Suite 4, Norvale, TX 70000 &nbsp;|&nbsp; Tel 555 010 2244 &nbsp;|&nbsp; kholbeck@brantovaseal.org &nbsp;|&nbsp; www.brantovaseal.org</div>
  </div>
  <div class="label letterhead-two-label">Letter Head Option 2</div>

  <!-- envelope backs -->
  <div class="piece envelope-back black">
    <svg class="trim" viewBox="0 0 214 66" preserveAspectRatio="none" aria-hidden="true">
      <rect width="214" height="66" fill="var(--brand-black)"/>
      <path d="M0 40 Q107 54 214 40 L214 66 L0 66 Z" fill="#2a2a2a"/>
    </svg>
  </div>
  <div class="piece envelope-back red">
    <svg class="trim" viewBox="0 0 214 66" preserveAspectRatio="none" aria-hidden="true">
      <path d="M0 0 L214 0 L214 34 Q107 50 0 34 Z" fill="var(--brand-red)"/>
    </svg>
  </div>
  <div class="piece envelope-back white">
    <svg class="trim" viewBox="0 0 214 66" preserveAspectRatio="none" aria-hidden="true">
      <path d="M0 32 Q107 48 214 32" fill="none" stroke="var(--paper-edge)" stroke-width="1"/>
    </svg>
  </div>

  <!-- envelope front -->
  <div class="piece envelope-front">
    <svg class="trim" viewBox="0 0 214 134" preserveAspectRatio="none" aria-hidden="true">
      <path d="M196 0 Q222 70 186 134 L214 134 L214 0 Z" fill="var(--brand-black)"/>
      <path d="M214 50 Q210 110 170 134 L186 134 Q208 104 214 76 Z" fill="var(--brand-red)"/>
    </svg>
    <div class="wordmark">Varn Tolq, Inc.</div>
    <div class="contact">120 Harbor Lane, Suite 4<br>Norvale, TX 70000</div>
  </div>
  <div class="label envelope-label">Envelope Option 2</div>
</body>
</html>
```